BSWC Steadwell Foot Health Care

Steadwell Foot Health Care guarantees to treat your foot problems in one visit or we will provide a free treatment session to you until you are completely satisfied.

10% discount for all new patients!

Mobile foot care at home!

Professional and fully qualified and insured foot health care practitioner

Expert advice

How to care for your feet

Treatments; Diabetic foot health, Corns, Callouses, Fungal Infections, Verrucas, Cracked Heels, Ingrowing Toenails, Ball of foot pain and Heel pain.

```html
<!DOCTYPE html>
<html lang="en">
<head>
<meta charset="utf-8">
<title>Feet Street News – BSWC Steadwell Foot Health Care</title>
<link href="https://fonts.googleapis.com/css2?family=Lato:wght@700;900&display=swap" rel="stylesheet">
<style>
  :root {
    --lime: #c6da6c;
    --lime-light: #d2e37f;
    --purple: #5f3a8e;
    --purple-dark: #3b2160;
    --forest: #1e3b21;
    --ink: #152015;
    --red: #e8262b;
    --orange: #f07a2b;
    --white: #ffffff;
    --skin: #e9c2aa;
  }
  * { box-sizing: border-box; margin: 0; padding: 0; }
  html, body { width: 1200px; height: 850px; overflow: hidden; background: #fff; }
  body { font-family: 'Lato', sans-serif; font-weight: 700; color: var(--ink); }
  .flyer { position: relative; width: 1200px; height: 850px; overflow: hidden; }
  .hero-photo {
    position: absolute; inset: 0;
    background: linear-gradient(100deg, #eef0ea 0%, #f4f1ee 45%, #f0d9cb 65%, #e6b89e 80%, #f3ece8 100%);
  }
  .panel { position: absolute; left: 82px; top: 0; width: 600px; height: 850px; background: var(--lime); }
  .title-band { position: absolute; left: 50px; top: 48px; width: 664px; height: 122px; }
  .title-band svg { position: absolute; inset: 0; }
  .title-band h1 {
    position: relative; text-align: center; color: var(--white);
    font-weight: 900; font-size: 66px; line-height: 122px; letter-spacing: -0.5px;
  }
  .intro {
    position: absolute; left: 82px; top: 182px; width: 600px; text-align: center;
    font-size: 22px; line-height: 31px;
  }
  .intro .deal { color: var(--red); font-size: 26px; }
  .guarantee {
    position: absolute; left: 82px; top: 292px; width: 600px; height: 106px;
    background: var(--white); border-left: 12px solid var(--purple); border-right: 12px solid var(--purple);
    text-align: center; padding-top: 10px;
  }
  .guarantee h2 { font-size: 26px; line-height: 32px; color: var(--ink); }
  .guarantee p { font-size: 13.5px; margin-top: 8px; }
  .before-after {
    position: absolute; left: 101px; top: 416px; width: 210px; height: 140px;
    background: var(--white); padding: 5px; display: flex; gap: 5px;
  }
  .before-after .shot {
    flex: 1; background: linear-gradient(180deg, #3a2e28, #d9a98c 55%, #3b2f29);
    position: relative;
  }
  .before-after .shot span {
    position: absolute; left: 0; right: 0; top: 68px; text-align: center; font-size: 12px; color: #2a2220;
  }
  .care-copy { position: absolute; left: 322px; top: 414px; width: 350px; font-size: 16px; line-height: 20.8px; }
  .specialism {
    position: absolute; left: 82px; top: 570px; width: 600px; height: 36px;
    background: var(--forest); color: var(--white); text-align: center; font-size: 19px; line-height: 36px;
  }
  .treatments {
    position: absolute; left: 82px; top: 610px; width: 600px; text-align: center;
    font-size: 14.8px; line-height: 19.5px;
  }
  .treatment-photo {
    position: absolute; top: 654px; height: 100px; background: var(--white); padding: 5px;
  }
  .treatment-photo div { width: 100%; height: 100%; background: linear-gradient(135deg, #1f3552, #e9d6c8 50%, #6b4a3a); }
  .home-visit {
    position: absolute; left: 82px; top: 766px; width: 600px; text-align: center;
    font-size: 21px; line-height: 28px;
  }
  .badge { position: absolute; top: 26px; height: 70px; border: 2px solid var(--lime); }
  .badge.register { left: 964px; width: 124px; background: var(--white); }
  .badge.alliance { left: 1094px; width: 72px; background: var(--forest); }
  .booking {
    position: absolute; left: 690px; top: 718px; width: 490px; text-align: center;
    font-size: 19px; line-height: 24px; color: var(--ink);
  }
  .call-now { position: absolute; left: 684px; top: 778px; width: 210px; height: 40px; }
  .call-now svg { position: absolute; inset: 0; }
  .call-now span {
    position: relative; display: block; padding-left: 14px; line-height: 40px;
    color: var(--white); font-size: 26px; font-weight: 900;
  }
  .phone {
    position: absolute; left: 902px; top: 772px; font-size: 42px; font-weight: 900;
    color: var(--forest); line-height: 52px; letter-spacing: 0.5px;
  }
</style>
</head>
<body>
<main class="flyer">
  <div class="hero-photo" role="img" aria-label="Photograph of a pair of bare feet resting on a white towel"></div>

  <div class="badge register" role="img" aria-label="Accredited register badge"></div>
  <div class="badge alliance" role="img" aria-label="Practitioner alliance membership badge"></div>

  <section class="panel"></section>

  <header class="title-band">
    <svg width="664" height="122" viewBox="0 0 664 122" aria-hidden="true">
      <polygon points="0,12 32,-12 32,12" fill="var(--purple-dark)"/>
      <polygon points="664,12 632,-12 632,12" fill="var(--purple-dark)"/>
      <polygon points="0,110 32,134 32,110" fill="var(--purple-dark)"/>
      <polygon points="664,110 632,134 632,110" fill="var(--purple-dark)"/>
      <rect x="0" y="12" width="664" height="98" fill="var(--purple)"/>
    </svg>
    <h1>Feet Street News!!!</h1>
  </header>

  <p class="intro">Newly arrived mobile foot care at home is in now<br>
    available in your area <span class="deal">10% Discounts</span> for all new<br>
    patients CALL NOW to register 07700900481</p>

  <section class="guarantee">
    <h2>BSWC Steadwell Foot Health Care Guarantees<br>to treat your foot problems in one visit</h2>
    <p>or we will provide a free treatment session to you until you’re completely satisfied</p>
  </section>

  <div class="before-after">
    <div class="shot" role="img" aria-label="Cracked heel before treatment"><span>Before</span></div>
    <div class="shot" role="img" aria-label="Smooth heel after treatment"><span>After</span></div>
  </div>

  <p class="care-copy">From as little as 30 per treatment session our fully qualified and insured Foot Health Care Practitioner will immediately bring you pain relief while also offering you professional expert advice on how to care for your feet and keep them looking good all year round.</p>

  <div class="specialism">Specialising in Diabetic foot health and Elderly foot care</div>

  <p class="treatments">10% off TREATMENTS Corns, Calluses, Fungal infections, Verruca’s, Cracked<br>heels, In growing toenails, Ball of foot pain, Heel pain and Diabetic Foot Health.</p>

  <div class="treatment-photo" style="left:96px;width:208px"><div role="img" aria-label="Practitioner in gloves treating toes"></div></div>
  <div class="treatment-photo" style="left:315px;width:186px"><div role="img" aria-label="Gloved hands treating the sole of a foot"></div></div>
  <div class="treatment-photo" style="left:512px;width:157px"><div role="img" aria-label="Foot treatment in progress in a clinic"></div></div>

  <p class="home-visit">We will conveniently visit you in your own home or<br>place of work which ever you find more comfortable</p>

  <p class="booking">to book an appointment with BSWC<br>Ms R T Moss DipCFHP Foot Health care Practitioner</p>

  <div class="call-now">
    <svg width="210" height="40" viewBox="0 0 210 40" aria-hidden="true">
      <polygon points="0,0 188,0 200,20 188,40 0,40" fill="var(--orange)"/>
      <polyline points="194,2 207,20 194,38" fill="none" stroke="var(--orange)" stroke-width="3"/>
    </svg>
    <span>CALL NOW!!!</span>
  </div>
  <div class="phone">0770090481</div>
</main>
</body>
</html>
```